ALL TEXT Social Media Graphics

We are looking for a series of social media graphics for Instagram (new size: 4:5 (1080 x 1350 pixels) ratio that are ALL TEXT. We want the following quotes below on each graphic; one quote per graphic. AND, In very small letters at the bottom of each graphic, add @PaulaWrenLive
The look and feel of these graphics should be complimentary to the color palette attached below; but keep them simple. But the design is up to you; at the end of this document, I provided various samples of all text graphics that I like as examples.
The Quotes are in the attached WORD document
women trying to lose weight

```html
<!DOCTYPE html>
<html lang="en">
<head>
<meta charset="utf-8">
<title>Golden Season Glow-Up – Instagram Text Series</title>
<link href="https://fonts.googleapis.com/css2?family=Saira:wdth,wght@100..125,500..600&display=swap" rel="stylesheet">
<style>
  :root {
    --page: #f6f6f6;
    --card: #ffffff;
    --band: #fdf2f7;
    --berry: #a8175a;
    --rose: #ef6a9f;
  }
  * { margin: 0; padding: 0; box-sizing: border-box; }
  html, body { width: 1200px; height: 632px; overflow: hidden; }
  body {
    background: var(--page);
    font-family: "Saira", "Arial", sans-serif;
    font-stretch: 108%;
    font-weight: 600;
    color: var(--berry);
    position: relative;
  }
  .post {
    position: absolute;
    width: 198px;
    height: 247px;
    background: var(--card);
    display: flex;
    flex-direction: column;
  }
  .post__headline {
    height: var(--head);
    padding: 10px 9px 0 10px;
    font-size: 19px;
    line-height: 24px;
    letter-spacing: -0.1px;
  }
  .post__support {
    height: var(--mid);
    background: var(--band);
    padding: 0 9px 0 10px;
    display: flex;
    align-items: center;
    font-size: 15px;
    line-height: 18.5px;
  }
  .post__cta {
    flex: 1;
    padding: 0 9px 0 10px;
    display: flex;
    align-items: center;
    font-size: 15px;
    line-height: 20px;
  }
  .post__handle {
    height: 20px;
    padding: 0 10px;
    font-size: 6px;
    font-weight: 500;
    line-height: 1;
    color: var(--berry);
  }
  .accent { color: var(--rose); }
  .main { color: var(--berry); }
</style>
</head>
<body>

<!-- Row one -->
<article class="post" style="left:48px;top:34px;--head:110px;--mid:69px">
  <h2 class="post__headline">You Can Absolutely <span class="accent">Be Down 20—30 Pounds</span> By End of Summer.</h2>
  <p class="post__support"><span>All It Takes Is The Right Plan - &amp; You’ve Found It.</span></p>
  <p class="post__cta" style="font-size:12px;line-height:15.5px"><span>Comment <span class="accent">“Glow”</span> for the Golden Season Glow-Up!</span></p>
  <p class="post__handle">@PaulaWrenLive</p>
</article>

<article class="post" style="left:274px;top:34px;--head:110px;--mid:69px">
  <h2 class="post__headline" style="font-size:19.5px;line-height:24.5px">You Don’t Need Another Diet - <span class="accent">You Need A System That Works.</span></h2>
  <p class="post__support" style="line-height:20px"><span>Drop 30 Pounds With The Golden Season Glow-Up</span></p>
  <p class="post__cta accent"><span>Comment <span class="main">“Summer”</span> To Start Now.</span></p>
  <p class="post__handle">@PaulaWrenLive</p>
</article>

<article class="post" style="left:499px;top:34px;--head:110px;--mid:69px">
  <h2 class="post__headline" style="font-size:19.5px;line-height:24.5px">This Summer Ain’t Over - and Neither Are <span class="accent">Your Body Goals.</span></h2>
  <p class="post__support" style="font-size:14px;line-height:18px"><span>Drop 30 Pounds <span class="accent">With The Golden Season Glow-Up.</span></span></p>
  <p class="post__cta"><span>Comment <span class="accent">“Glow”</span> To Get The Plan</span></p>
  <p class="post__handle">@PaulaWrenLive</p>
</article>

<article class="post" style="left:725px;top:34px;--head:148px;--mid:69px">
  <h2 class="post__headline" style="font-size:20px;line-height:26px">If Your Goal Is A Tiny Waist, <span class="accent">Flat Belly &amp; 30 Pounds Down -</span> This Is The Plan</h2>
  <p class="post__support accent" style="line-height:20px"><span>Comment <span class="main">“Summer”</span> To Join The Golden Season Glow-Up!</span></p>
  <p class="post__cta"></p>
  <p class="post__handle">@PaulaWrenLive</p>
</article>

<article class="post" style="left:952px;top:34px;--head:122px;--mid:68px">
  <h2 class="post__headline" style="font-size:20px;line-height:26px">There’s Still Time <span class="accent">To Drop The 30 Pounds and</span> Slay This Summer.</h2>
  <p class="post__support" style="font-size:13.5px;line-height:16.5px"><span>The Golden Season Glow-Up Has The Blueprint.</span></p>
  <p class="post__cta"><span>Comment <span class="accent">“Glow”!</span></span></p>
  <p class="post__handle">@PaulaWrenLive</p>
</article>

<!-- Row two -->
<article class="post" style="left:49px;top:334px;--head:148px;--mid:69px">
  <h2 class="post__headline" style="font-size:17px;line-height:21px">Snatched Waist, Flat Tummy, <span class="accent">30 Pounds Lighter -</span> that’s What The Golden <span class="accent">Season Glow-Up Challenge</span> Delivers.</h2>
  <p class="post__support" style="font-size:16px;line-height:20.5px"><span>Comment <span class="accent">“Glow”</span> To Get The Plan</span></p>
  <p class="post__cta"></p>
  <p class="post__handle">@PaulaWrenLive</p>
</article>

<article class="post" style="left:275px;top:334px;--head:119px;--mid:68px">
  <h2 class="post__headline" style="font-size:19.5px;line-height:24.5px">Nothing Feels Better Than Seeing That <span class="accent">Scale Drop Week After Week.</span></h2>
  <p class="post__support" style="line-height:17.5px"><span>Let’s Lose Up To 30 Pounds This Summer - Together.</span></p>
  <p class="post__cta" style="font-size:11px;line-height:13.5px"><span>Comment <span class="accent">“Summer”</span> To Join The Golden Season Glow-Up!</span></p>
  <p class="post__handle">@PaulaWrenLive</p>
</article>

<article class="post" style="left:501px;top:334px;--head:121px;--mid:68px">
  <h2 class="post__headline" style="font-size:19.5px;line-height:24.5px">Sis,We’re Dropping <span class="accent">Belly Flat</span> &amp; Saying <span class="accent">Goodbye To</span> Stubborn Pounds</h2>
  <p class="post__support" style="font-size:17.5px;line-height:21px"><span><span class="accent">Join The Golden</span> Season Glow-Up</span></p>
  <p class="post__cta" style="font-size:16px"><span>Comment <span class="accent">“Summer”!</span></span></p>
  <p class="post__handle">@PaulaWrenLive</p>
</article>

<article class="post" style="left:727px;top:334px;--head:119px;--mid:69px">
  <h2 class="post__headline" style="font-size:26px;line-height:33px;padding-top:11px"><span class="accent">Don’t Wait</span> ‘till Next Summer To Get Right.</h2>
  <p class="post__support" style="font-size:14px;line-height:19px"><span>The Time Is NOW. <span class="accent">Drop 30 Pounds</span> With The Golden <span class="accent">Season Glow-Up</span></span></p>
  <p class="post__cta" style="font-size:16px"><span>Comment <span class="accent">“Summer”!</span></span></p>
  <p class="post__handle">@PaulaWrenLive</p>
</article>

<article class="post" style="left:951px;top:334px;--head:120px;--mid:69px">
  <h2 class="post__headline" style="font-size:19.5px;line-height:24.5px">You’ve Got 8 Weeks And The Perfect Plan To <span class="accent">Drop 30 Pounds</span></h2>
  <p class="post__support" style="font-size:14.5px;line-height:18.5px"><span><span class="accent">Let’s Get Snatched This Summer</span> With The Golden Season Glow-Up.</span></p>
  <p class="post__cta" style="font-size:16px"><span>Comment <span class="accent">“Summer”!</span></span></p>
  <p class="post__handle">@PaulaWrenLive</p>
</article>

</body>
</html>
```